Logo and 1 page Flyer for Meridian Fund

We need a logo and a 1 single page flyer for an Investment Fund we'll distribute worldwide. It'a Meridian Fund that will give a return also to the poorest people in the world. Details inside. We give just an idea (based on a previous flyer we had here) with the attached draft. Anyone can figure out how to make its own. NOTE: LQV is our company's logo.

Target Market(s)

Investors

Industry/Entity Type

Finance And Accounting

Logo Text

KOLB Kindred Open Bloom Fund

Font styles to use
Serif

Colors
00a990

Requirements
Must have
• A logo you choose which should be:
• - Elegant
• - Innovative
• - Crypto evoking (Company launching is a cripto company)
• - Hi tech
Nice to have
• We have sent you all materials to be able to understand:
• 1. A draft of how we would like the texts to come out. Don't use this (we're already using with other texts), ,but see the evidence of Logo, Slogan, and the 3 main characteristics. Also notice very well that is very elegant. Use a real light on color, make it as shining as you can. It must be a sort of shining green, expressing Hope, Beauty, Well being
• 2. The logo for LQV that is the company launching the project. In draft you see on low left. You can put wherever you feel right
• 3. All texts are on draft to be seen, and on word to be used. You can choose font and dimensions as you prefer
• 4. We've given you logo we have for PIRO. If you feel, you can use in the line where we talk about it or place somewhere. Not mandatory
Should not have
• Funny things; too commercial style; unprofessional aspect

```html
<!DOCTYPE html>
<html lang="en">
<head>
<meta charset="utf-8">
<title>KOLB – Kindred Open Bloom Fund</title>
<link rel="stylesheet" href="https://fonts.googleapis.com/css2?family=Cinzel:wght@400;500&family=Montserrat:wght@400;500;600&display=swap">
<style>
  :root {
    --page-bg: #e9e7e3;
    --blue-deep: #0d4a9e;
    --blue-main: #1560b8;
    --blue-light: #3f8ee0;
    --teal: #1db3a0;
    --teal-line: #27c4b0;
    --white: #ffffff;
    --footer-ink: #1f5fae;
    --grey-ink: #6f7680;
  }
  * { margin: 0; padding: 0; box-sizing: border-box; }
  html, body {
    width: 1116px; height: 1200px; overflow: hidden;
    background: var(--page-bg);
  }
  .flyer {
    position: absolute; left: 122px; top: 37px;
    width: 871px; height: 1125px;
    background: var(--white);
    font-family: "Montserrat", Arial, sans-serif;
    color: var(--white);
    overflow: hidden;
  }
  .hero {
    position: absolute; left: 0; top: 0; width: 871px; height: 994px;
    background:
      radial-gradient(ellipse 70% 18% at 55% 12%, rgba(120,190,255,.45), transparent 70%),
      linear-gradient(180deg, var(--blue-main) 0%, var(--blue-deep) 100%);
    overflow: hidden;
  }
  .tech-visual {
    position: absolute; left: 560px; top: 330px; width: 520px; height: 560px;
    border-radius: 50%;
    background: radial-gradient(circle at 45% 45%, rgba(140,200,255,.55) 0%, rgba(70,140,230,.35) 35%, rgba(30,100,200,.15) 60%, transparent 72%);
  }
  .tech-glow {
    position: absolute; left: -60px; top: 740px; width: 420px; height: 300px;
    background: radial-gradient(ellipse at center, rgba(90,160,240,.35), transparent 70%);
  }
  .brand-dot {
    position: absolute; left: 60px; top: 68px; width: 205px; height: 205px;
    border-radius: 50%; background: var(--white);
  }
  .brand-name {
    position: absolute; left: 289px; top: 60px;
    font-family: "Cinzel", "Times New Roman", serif; font-weight: 400;
    font-size: 200px; line-height: 1; letter-spacing: 0;
    color: var(--white);
  }
  .brand-tagline {
    position: absolute; left: 290px; top: 256px; width: 510px;
    font-size: 19px; font-weight: 500; letter-spacing: .47em;
    white-space: nowrap; color: var(--white);
  }
  .brand-rule {
    position: absolute; left: 62px; top: 294px; width: 737px; height: 3px;
    background: var(--teal-line);
  }
  .headline {
    position: absolute; left: 92px; top: 367px;
    font-size: 31px; font-weight: 600; line-height: 40px;
  }
  .intro {
    position: absolute; left: 92px; top: 470px; width: 440px;
    font-size: 19px; line-height: 31px; font-weight: 400;
  }
  .feature {
    position: absolute; left: 92px; width: 760px; height: 60px;
  }
  .feature-tag {
    position: absolute; left: 0; top: 0; width: 196px; height: 42px;
    background: var(--teal);
    font-size: 19px; font-weight: 600; line-height: 42px; text-align: center;
  }
  .feature-text {
    position: absolute; left: 218px; top: 6px;
    font-size: 19px; line-height: 31px; white-space: nowrap;
  }
  .footer {
    position: absolute; left: 0; top: 994px; width: 871px; height: 131px;
    background: var(--white);
  }
  .partner {
    position: absolute; top: 38px; display: flex; align-items: center; gap: 10px;
    font-family: "Montserrat", Arial, sans-serif; font-weight: 600; font-size: 40px;
  }
  .partner-piro { left: 70px; color: var(--grey-ink); }
  .partner-piro .mark { width: 14px; height: 14px; background: var(--grey-ink); }
  .partner-lqv { left: 350px; color: var(--footer-ink); }
  .partner-lqv .mark { width: 42px; height: 42px; border-radius: 50%; background: var(--footer-ink); }
  .web-link {
    position: absolute; left: 586px; top: 47px; width: 232px; height: 31px;
    background: var(--teal); color: var(--white);
    font-size: 17px; font-weight: 500; line-height: 31px; text-align: center;
  }
</style>
</head>
<body>
  <main class="flyer">
    <section class="hero">
      <div class="tech-visual" role="img" aria-label="Glowing high-tech digital coin and circuit rings in blue tones"></div>
      <div class="tech-glow" role="img" aria-label="Soft blue digital network glow"></div>

      <div class="brand-dot"></div>
      <h1 class="brand-name">KOLB</h1>
      <p class="brand-tagline">KINDRED OPEN BLOOM FUND</p>
      <div class="brand-rule"></div>

      <h2 class="headline">Raise the Poor<br>surfing with us</h2>
      <p class="intro">With KOLB you achieve sound return on<br>your investment. And you help needy<br>ones to obtain real help in their life.</p>

      <div class="feature" style="top:627px">
        <span class="feature-tag">Better RETURN</span>
        <p class="feature-text">| Using PIRO - Predictive Intelligent Routing<br>Optimizer. A breaktrough in money management</p>
      </div>
      <div class="feature" style="top:714px">
        <span class="feature-tag">For ANYONE</span>
        <p class="feature-text">| For those who can invest. And for those<br>Who have no money to survive.</p>
      </div>
      <div class="feature" style="top:801px">
        <span class="feature-tag">Better RETURN</span>
        <p class="feature-text">| To have a return that<br>Warms you and others.</p>
      </div>
    </section>

    <footer class="footer">
      <div class="partner partner-piro"><span class="mark"></span>PIRO</div>
      <div class="partner partner-lqv"><span class="mark"></span>LQV</div>
      <div class="web-link">www.lqvfund.io</div>
    </footer>
  </main>
</body>
</html>
```